Business Card Design Project

Hello,

I am job searching in Canada and need a professional / nice looking business card to give away in networking meetings and informational interviews.

I have extensive market development and business growth experience with strong marketing and project management background.

You'll find specific information about my profile at: http://ca.proventa.example/in/brunomarquezprofile/

My objective is to work for canadian companies trying to expand their business to Latin America or Hispanic market; or for foreign companies trying to introduce their business to Canada.

Thanks for your help.

Bruno Marquez

Target Market(s)

Canadian companies trying to expand their business to Latin America or Hispanic market; foreign companies trying to introduce their business to Canada

Industry/Entity Type

Marketing

Requirements
Must have
• The Business card must be two sided, one side must be white, and the other color may be any of the following (or similar):
Green - PMS 349C
Dark Green - PMS 3435
Teal - PMS 315C
Bright Blue - PMS 285C
Earth Brown - PMS 438C
Neutral Gray - PMS 423C
Charcoal Gray - PMS 425C
Silver (metallic) - PMS 877C

Spot UV will be used in the front side to illuminate words or designs so that they reflect and gleam in the light, giving the card a multi-textured look and feel.
Nice to have
• I have attached a QR Code sample as an option to have somewhere in the business card to link it to my Proventa account instead of having written the long Proventa address.

It is not a requirement to have it, however, just in case you think is a good idea to have it on the business card.

```html
<!DOCTYPE html>
<html lang="en">
<head>
<meta charset="utf-8">
<title>Bruno Marquez — Business Card Colourways</title>
<link rel="stylesheet" href="https://fonts.googleapis.com/css2?family=Jost:ital,wght@0,300;0,400;1,300&display=swap">
<style>
  :root {
    --page: #ffffff;
    --card-white: #ffffff;
    --ink: #1a1a1a;
    --ink-soft: #8a8a8a;
    --rule: #b5b5b5;
    --green: #00920f;
    --dark-green: #005614;
    --teal: #009484;
    --bright-blue: #1e90ff;
    --earth: #3a4600;
    --charcoal: #3a3a3a;
  }
  * { box-sizing: border-box; margin: 0; padding: 0; }
  html, body { width: 1200px; height: 1000px; overflow: hidden; background: var(--page); }
  body { position: relative; font-family: "Jost", sans-serif; color: var(--ink); }

  .card {
    position: absolute;
    width: 363px;
    height: 217px;
    box-shadow: 0 6px 14px rgba(0,0,0,0.16);
  }
  .card--front { background: var(--card-white); }
  .card--back { display: flex; align-items: center; justify-content: center; }

  .monogram {
    position: absolute;
    left: 50%;
    top: 31px;
    width: 42px;
    height: 42px;
    margin-left: -21px;
    border-radius: 50%;
    color: #fff;
    display: flex;
    align-items: center;
    justify-content: center;
    font-weight: 300;
    font-size: 17px;
    letter-spacing: 0.5px;
  }
  .name {
    position: absolute;
    top: 89px;
    width: 100%;
    text-align: center;
    font-size: 13px;
    font-weight: 400;
    letter-spacing: 2px;
  }
  .title {
    position: absolute;
    top: 106px;
    width: 100%;
    text-align: center;
    font-size: 6.5px;
    font-style: italic;
    font-weight: 300;
    letter-spacing: 1px;
    color: var(--ink-soft);
  }
  .contact {
    position: absolute;
    left: 67px;
    top: 135px;
    width: 226px;
    border-top: 1px solid var(--rule);
    border-bottom: 1px solid var(--rule);
    list-style: none;
  }
  .contact__row {
    display: flex;
    justify-content: space-between;
    align-items: center;
    height: 18px;
    font-size: 8.5px;
    font-weight: 300;
    letter-spacing: 1px;
    border-bottom: 1px dashed var(--rule);
  }
  .contact__row:last-child { border-bottom: none; }
  .contact__label { font-weight: 400; font-size: 7.5px; letter-spacing: 0; }
  .contact__value--phone { color: var(--ink-soft); font-style: italic; }

  .seal {
    width: 68px;
    height: 68px;
    border-radius: 50%;
    border: 1px solid rgba(255,255,255,0.45);
    color: #fff;
    display: flex;
    align-items: center;
    justify-content: center;
    font-weight: 300;
    font-size: 28px;
    letter-spacing: 0.5px;
  }

  .tone-green { background: var(--green); }
  .tone-dark-green { background: var(--dark-green); }
  .tone-teal { background: var(--teal); }
  .tone-blue { background: var(--bright-blue); }
  .tone-earth { background: var(--earth); }
  .tone-charcoal { background: var(--charcoal); }
</style>
</head>
<body>

  <!-- Row 1: fronts -->
  <section class="card card--front" style="left:27px;top:24px">
    <div class="monogram tone-green">BM</div>
    <h1 class="name">BRUNO MARQUEZ</h1>
    <p class="title">TITLE HERE</p>
    <ul class="contact">
      <li class="contact__row"><span class="contact__label">P:</span><span class="contact__value contact__value--phone">604.555.0182</span></li>
      <li class="contact__row"><span class="contact__label">E:</span><span class="contact__value">bruno@brunomarquez.ca</span></li>
      <li class="contact__row"><span class="contact__label">W:</span><span class="contact__value">proventa.example/in/brunomarquezprofile</span></li>
    </ul>
  </section>
  <section class="card card--front" style="left:416px;top:24px">
    <div class="monogram tone-dark-green">BM</div>
    <h1 class="name">BRUNO MARQUEZ</h1>
    <p class="title">TITLE HERE</p>
    <ul class="contact">
      <li class="contact__row"><span class="contact__label">P:</span><span class="contact__value contact__value--phone">604.555.0182</span></li>
      <li class="contact__row"><span class="contact__label">E:</span><span class="contact__value">bruno@brunomarquez.ca</span></li>
      <li class="contact__row"><span class="contact__label">W:</span><span class="contact__value">proventa.example/in/brunomarquezprofile</span></li>
    </ul>
  </section>
  <section class="card card--front" style="left:805px;top:24px">
    <div class="monogram tone-teal">BM</div>
    <h1 class="name">BRUNO MARQUEZ</h1>
    <p class="title">TITLE HERE</p>
    <ul class="contact">
      <li class="contact__row"><span class="contact__label">P:</span><span class="contact__value contact__value--phone">604.555.0182</span></li>
      <li class="contact__row"><span class="contact__label">E:</span><span class="contact__value">bruno@brunomarquez.ca</span></li>
      <li class="contact__row"><span class="contact__label">W:</span><span class="contact__value">proventa.example/in/brunomarquezprofile</span></li>
    </ul>
  </section>

  <!-- Row 2: backs -->
  <section class="card card--back tone-green" style="left:27px;top:264px"><div class="seal">BM</div></section>
  <section class="card card--back tone-dark-green" style="left:416px;top:264px"><div class="seal">BM</div></section>
  <section class="card card--back tone-teal" style="left:805px;top:264px"><div class="seal">BM</div></section>

  <!-- Row 3: fronts -->
  <section class="card card--front" style="left:27px;top:510px">
    <div class="monogram tone-blue">BM</div>
    <h1 class="name">BRUNO MARQUEZ</h1>
    <p class="title">TITLE HERE</p>
    <ul class="contact">
      <li class="contact__row"><span class="contact__label">P:</span><span class="contact__value contact__value--phone">604.555.0182</span></li>
      <li class="contact__row"><span class="contact__label">E:</span><span class="contact__value">bruno@brunomarquez.ca</span></li>
      <li class="contact__row"><span class="contact__label">W:</span><span class="contact__value">proventa.example/in/brunomarquezprofile</span></li>
    </ul>
  </section>
  <section class="card card--front" style="left:419px;top:510px">
    <div class="monogram tone-earth">BM</div>
    <h1 class="name">BRUNO MARQUEZ</h1>
    <p class="title">TITLE HERE</p>
    <ul class="contact">
      <li class="contact__row"><span class="contact__label">P:</span><span class="contact__value contact__value--phone">604.555.0182</span></li>
      <li class="contact__row"><span class="contact__label">E:</span><span class="contact__value">bruno@brunomarquez.ca</span></li>
      <li class="contact__row"><span class="contact__label">W:</span><span class="contact__value">proventa.example/in/brunomarquezprofile</span></li>
    </ul>
  </section>
  <section class="card card--front" style="left:807px;top:510px">
    <div class="monogram tone-charcoal">BM</div>
    <h1 class="name">BRUNO MARQUEZ</h1>
    <p class="title">TITLE HERE</p>
    <ul class="contact">
      <li class="contact__row"><span class="contact__label">P:</span><span class="contact__value contact__value--phone">604.555.0182</span></li>
      <li class="contact__row"><span class="contact__label">E:</span><span class="contact__value">bruno@brunomarquez.ca</span></li>
      <li class="contact__row"><span class="contact__label">W:</span><span class="contact__value">proventa.example/in/brunomarquezprofile</span></li>
    </ul>
  </section>

  <!-- Row 4: backs -->
  <section class="card card--back tone-blue" style="left:27px;top:750px"><div class="seal">BM</div></section>
  <section class="card card--back tone-earth" style="left:419px;top:750px"><div class="seal">BM</div></section>
  <section class="card card--back tone-charcoal" style="left:807px;top:750px"><div class="seal">BM</div></section>

</body>
</html>
```